Real Estate Sign to Help Modernize and Make it POP!

Design a sign style that would be good for marketing the sale or lease of properties. This will be 3 ' x 4' when printed and needs to look professional, modern, and catchy. It should us the company name, logo, and phone number at a minimum. Keep with the color scheme but open to varieties.

It will be printed and put in a large wooden frame as shown in one of the pictures.

Target Market(s)

Buyers and Tenants

Industry/Entity Type

Real Estate

Requirements
Must have
• company name, logo, and phone number
same color scheme as sign and website
Nice to have
• My Name, "Merrick Halvane, CCIM"
Company Website
Ability to have an easy change from FOR SALE to FOR LEASE or FOR SALE/LEASE when I need to move this sign to a new property
An ability to have reflective colors printed on the contrast for cars to see at night
Should not have
• "Property Managed by"

```html
<!DOCTYPE html>
<html lang="en">
<head>
<meta charset="utf-8">
<title>Alderwood Realty – For Sale Sign</title>
<link rel="stylesheet" href="https://fonts.googleapis.com/css2?family=Montserrat:wght@600;800&family=Oswald:wght@600&family=Roboto:wght@700&display=swap">
<style>
  :root {
    --brand-green: #42615e;
    --slate: #383f4a;
    --paper: #ffffff;
  }
  html, body {
    margin: 0;
    padding: 0;
    width: 1200px;
    height: 1200px;
    overflow: hidden;
    background: var(--paper);
  }
  .canvas {
    position: relative;
    width: 1200px;
    height: 1200px;
  }
  .sign {
    position: absolute;
    left: 172px;
    top: 280px;
    width: 865px;
    height: 648px;
  }
  .band { fill: var(--slate); }
  .brand-field { fill: var(--brand-green); }
  .brand-disc { fill: var(--brand-green); stroke: var(--paper); stroke-width: 7; }
  .sign-face { fill: var(--paper); }
  .agent-name {
    font-family: "Roboto", Arial, sans-serif;
    font-weight: 700;
    font-size: 31px;
    fill: var(--paper);
  }
  .status {
    font-family: "Montserrat", Arial, sans-serif;
    font-weight: 800;
    font-size: 150px;
    fill: var(--brand-green);
  }
  .phone {
    font-family: "Oswald", "Arial Narrow", sans-serif;
    font-weight: 600;
    font-size: 66px;
    fill: var(--paper);
  }
  .website {
    font-family: "Oswald", "Arial Narrow", sans-serif;
    font-weight: 600;
    font-size: 34px;
    fill: var(--paper);
  }
  .brand-name {
    font-family: "Montserrat", Arial, sans-serif;
    font-weight: 600;
    font-size: 34px;
    fill: var(--paper);
  }
</style>
</head>
<body>
<div class="canvas">
  <svg class="sign" viewBox="0 0 865 648" xmlns="http://www.w3.org/2000/svg" role="group" aria-label="For sale sign">
    <defs>
      <clipPath id="sign-clip"><rect width="865" height="648"/></clipPath>
    </defs>
    <g clip-path="url(#sign-clip)">
      <rect class="sign-face" width="865" height="648"/>
      <rect class="band band-top" x="300" y="34" width="565" height="80"/>
      <rect class="band band-bottom" x="0" y="454" width="865" height="194"/>
      <rect class="brand-field" x="0" y="0" width="92" height="648"/>
      <circle class="brand-disc" cx="92" cy="320" r="370"/>
      <rect class="brand-field" x="0" y="0" width="88" height="648"/>
    </g>

    <text class="brand-name" x="234" y="344" text-anchor="middle">ALDERWOOD REALTY</text>

    <text class="agent-name" x="831" y="87" text-anchor="end">MERRICK HALVANE, CCIM</text>

    <text class="status" x="831" y="279" text-anchor="end" textLength="338" lengthAdjust="spacingAndGlyphs">FOR</text>
    <text class="status" x="831" y="391" text-anchor="end" textLength="338" lengthAdjust="spacingAndGlyphs">SALE</text>

    <text class="phone" x="831" y="545" text-anchor="end" textLength="366" lengthAdjust="spacingAndGlyphs">504-217--6630</text>
    <text class="website" x="831" y="608" text-anchor="end">ALDERWOODREALTY.COM</text>
  </svg>
</div>
</body>
</html>
```